Vehicles Brochure Diagram

Task Outline
Create diagrams for our new vehicles brochures

Task Description

Who are we:
TLR is New Zealand's largest Business Group Buying organisation, helping organisations nationwide reduce their running costs. We offer members the best deals from over 100 Contracted Suppliers, anything from vehicles, stationery to electronics and coffee.

The project:
We need 2 diagrams to illustrate the benefits of our vehicle services. The diagram will be used in our brochures (example attached)

1. A Diagram illustrating/explaining the elements that are involved in purchasing a new car & how our service ties it all together to provide the best solution.
- Please see the Diagram 1 PDF for a rough wireframe of the elements involved

2. Another small diagram inserted on an separate page to demonstrate how our services can increase safety & profit and reduce costs & risks (PDF: Diagram 2 Details)

The design needs to be clean, clear and simple that it’s easy to understand within a few seconds of looking at it. Feel free to explore with different elements in the realm of infographics, flowcharts & diagrams to best communicate the idea visually.
Updates

Just thought I’ll share some of the feedback we’re giving tosubmissions that have been coming through to help with new submissions

-Challenge & be creative about the ways you demonstratethe elements

-We don’t want to see your design replicating the ones that isdrawn. The purpose of it is only to provide you with the content in context

-We can’t emphasis enough that the style pdf is only areference and not the look you should imitate. 

If you have any question please feel free to contact me.Looking forward to see your designs!

Reason: We're keen to see more approaches & creative ways of interpreting the content rather than a standard cycle diagram. Entries so far have been good but quite literal, we will provide feedback to help steer it in the right direction.

Target Market(s)

Business professionals, Decision makers on a corporate level & prospects.

Industry/Entity Type

Electronics

Requirements
Must have

• Likes – simple, clean & clear, uncluttered

Dislikes – Overcrowded images, text, & colours. Overly expressive typeface. Please no literal illustration of our sketches or colored version of our sketch.

Font: -Myriad Pro

Colour: Please refer to the color palette in the ‘Diagram Color & Style’ PDF

The brochures are attached with content to provide context that might inform the design better,

Dimensions & the amount of space you have to work with will also be highlighted

```html
<!DOCTYPE html>
<html lang="en">
<head>
<meta charset="utf-8">
<title>Vehicle Services Diagrams</title>
<link rel="stylesheet" href="https://fonts.googleapis.com/css2?family=Source+Sans+3:wght@400;600&display=swap">
<style>
  :root {
    --paper: #ffffff;
    --divider: #a8a8a8;
    --green-dark: #1d6a37;
    --green-light: #4f9c40;
    --blue-deep: #174a8b;
    --blue-mid: #2f7cc4;
    --blue-light: #7cc4ef;
    --title-blue: #8fd3f4;
    --label-green: #2a6b2c;
    --white: #ffffff;
  }
  html, body {
    margin: 0;
    padding: 0;
    width: 1200px;
    height: 835px;
    overflow: hidden;
    background: var(--paper);
  }
  .canvas {
    display: block;
    width: 1200px;
    height: 835px;
    font-family: "Source Sans 3", sans-serif;
  }
  .divider { fill: var(--divider); }
  .card-title { fill: var(--title-blue); font-size: 19px; font-weight: 400; }
  .card-detail { fill: var(--white); font-size: 11.5px; font-weight: 600; }
  .hub-label { fill: var(--white); font-size: 26px; font-weight: 400; text-anchor: middle; }
  .icon { fill: none; stroke: var(--white); stroke-width: 2.4; stroke-linejoin: round; stroke-linecap: round; }
  .icon-fill { fill: var(--white); }
  .gain-label { fill: var(--blue-deep); font-size: 18px; }
  .cut-label { fill: var(--label-green); font-size: 18px; text-anchor: end; }
  .axis-gain { fill: var(--blue-deep); font-size: 31px; letter-spacing: 1px; }
  .axis-cut { fill: var(--label-green); font-size: 31px; letter-spacing: 1px; }
</style>
</head>
<body>
<svg class="canvas" viewBox="0 0 1200 835" xmlns="http://www.w3.org/2000/svg">
  <defs>
    <linearGradient id="card-fill" x1="0" y1="0" x2="1" y2="1">
      <stop offset="0" stop-color="var(--green-dark)"/>
      <stop offset="1" stop-color="var(--green-light)"/>
    </linearGradient>
    <radialGradient id="hub-fill" cx="0.7" cy="0.45" r="0.8">
      <stop offset="0" stop-color="var(--blue-light)"/>
      <stop offset="0.5" stop-color="var(--blue-mid)"/>
      <stop offset="1" stop-color="var(--blue-deep)"/>
    </radialGradient>
    <linearGradient id="blade-fill" x1="0" y1="0" x2="1" y2="1">
      <stop offset="0" stop-color="#1b5499"/>
      <stop offset="0.6" stop-color="#3f8fd2"/>
      <stop offset="1" stop-color="#8cd0f3"/>
    </linearGradient>
    <linearGradient id="bar-blue" x1="0" y1="0" x2="1" y2="0">
      <stop offset="0" stop-color="#1f5da6"/>
      <stop offset="0.45" stop-color="#6fbbe9"/>
      <stop offset="1" stop-color="#2a6db5"/>
    </linearGradient>
    <linearGradient id="bar-green" x1="0" y1="0" x2="1" y2="0">
      <stop offset="0" stop-color="#1f6b35"/>
      <stop offset="0.45" stop-color="#5fae46"/>
      <stop offset="1" stop-color="#2a7a36"/>
    </linearGradient>
    <path id="blade" d="M -30,-98 A 102 102 0 0 1 74,-70 L 96,-88 L 106,-2 L 32,-38 L 56,-52 A 76 76 0 0 0 -26,-72 Z"/>
  </defs>

  <rect class="divider" x="578" y="0" width="12" height="835"/>

  <g class="cycle">
    <g class="hub" transform="translate(298 416)">
      <circle r="86" fill="url(#hub-fill)"/>
      <use href="#blade" fill="url(#blade-fill)"/>
      <use href="#blade" fill="url(#blade-fill)" transform="rotate(90)"/>
      <use href="#blade" fill="url(#blade-fill)" transform="rotate(180)"/>
      <use href="#blade" fill="url(#blade-fill)" transform="rotate(270)"/>
      <text class="hub-label" x="2" y="-8">Best fit</text>
      <text class="hub-label" x="2" y="24">for purpose</text>
    </g>

    <g class="card card-run">
      <rect x="290" y="216" width="193" height="107" rx="16" fill="url(#card-fill)"/>
      <text class="card-title" x="314" y="274">Run</text>
      <text class="card-detail" x="314" y="294">Fuel, Tyres, Rego,</text>
      <text class="card-detail" x="314" y="309">RoC</text>
      <g class="icon-pump">
        <rect class="icon" x="425" y="232" width="20" height="32" rx="2"/>
        <rect class="icon-fill" x="429" y="237" width="12" height="8"/>
        <path class="icon" d="M445 244 h5 v16 a3 3 0 0 0 6 0 v-18 l-5 -6"/>
        <rect class="icon-fill" x="420" y="264" width="30" height="4"/>
      </g>
    </g>

    <g class="card card-price">
      <rect x="11" y="313" width="194" height="120" rx="16" fill="url(#card-fill)"/>
      <text class="card-title" x="34" y="375">Price</text>
      <text class="card-detail" x="34" y="394">End of Life,</text>
      <text class="card-detail" x="34" y="409">Disposal Costs</text>
      <g class="icon-coins">
        <ellipse class="icon" cx="140" cy="340" rx="10" ry="4"/>
        <path class="icon" d="M130 340 v12 a10 4 0 0 0 20 0 v-12 M130 346 a10 4 0 0 0 20 0"/>
        <ellipse class="icon" cx="128" cy="360" rx="10" ry="4"/>
        <path class="icon" d="M118 360 v12 a10 4 0 0 0 20 0 v-12 M118 366 a10 4 0 0 0 20 0"/>
        <ellipse class="icon" cx="152" cy="362" rx="10" ry="4"/>
        <path class="icon" d="M142 362 v12 a10 4 0 0 0 20 0 v-12 M142 368 a10 4 0 0 0 20 0"/>
      </g>
    </g>

    <g class="card card-manage">
      <rect x="384" y="416" width="191" height="119" rx="16" fill="url(#card-fill)"/>
      <text class="card-title" x="406" y="483">Manage</text>
      <text class="card-detail" x="406" y="501">Lease, Finance &amp; Tax,</text>
      <text class="card-detail" x="406" y="516">Insurance</text>
      <g class="icon-calculator">
        <rect class="icon" x="519" y="432" width="24" height="34" rx="3"/>
        <rect class="icon-fill" x="523" y="436" width="16" height="7"/>
        <g class="icon-fill">
          <rect x="523" y="447" width="4" height="3"/><rect x="529" y="447" width="4" height="3"/><rect x="535" y="447" width="4" height="3"/>
          <rect x="523" y="453" width="4" height="3"/><rect x="529" y="453" width="4" height="3"/><rect x="535" y="453" width="4" height="3"/>
          <rect x="523" y="459" width="4" height="3"/><rect x="529" y="459" width="4" height="3"/><rect x="535" y="459" width="4" height="3"/>
        </g>
      </g>
    </g>

    <g class="card card-requirements">
      <rect x="117" y="518" width="191" height="119" rx="16" fill="url(#card-fill)"/>
      <text class="card-title" x="138" y="583">Requirements</text>
      <text class="card-detail" x="138" y="602">Safety, Sustainability,</text>
      <text class="card-detail" x="138" y="617">Specifications</text>
      <g class="icon-magnifier">
        <circle class="icon" cx="273" cy="550" r="11"/>
        <path class="icon" d="M280 559 l10 13" stroke-width="4"/>
      </g>
    </g>
  </g>

  <g class="bars">
    <g class="bar">
      <rect x="818" y="85" width="42" height="329" fill="url(#bar-blue)"/>
      <rect x="818" y="414" width="42" height="124" fill="url(#bar-green)"/>
      <ellipse cx="839" cy="538" rx="21" ry="5" fill="#2a7a36"/>
      <ellipse cx="839" cy="85" rx="21" ry="6" fill="#2567b0"/>
    </g>
    <g class="bar">
      <rect x="843" y="141" width="42" height="273" fill="url(#bar-blue)"/>
      <rect x="843" y="414" width="42" height="176" fill="url(#bar-green)"/>
      <ellipse cx="864" cy="590" rx="21" ry="5" fill="#2a7a36"/>
      <ellipse cx="864" cy="141" rx="21" ry="6" fill="#2567b0"/>
    </g>
    <g class="bar">
      <rect x="870" y="188" width="42" height="226" fill="url(#bar-blue)"/>
      <rect x="870" y="414" width="42" height="223" fill="url(#bar-green)"/>
      <ellipse cx="891" cy="637" rx="21" ry="5" fill="#2a7a36"/>
      <ellipse cx="891" cy="188" rx="21" ry="6" fill="#2567b0"/>
    </g>
    <g class="bar">
      <rect x="898" y="236" width="42" height="178" fill="url(#bar-blue)"/>
      <rect x="898" y="414" width="42" height="274" fill="url(#bar-green)"/>
      <ellipse cx="919" cy="688" rx="21" ry="5" fill="#2a7a36"/>
      <ellipse cx="919" cy="236" rx="21" ry="6" fill="#2567b0"/>
    </g>
    <g class="bar">
      <rect x="926" y="287" width="42" height="127" fill="url(#bar-blue)"/>
      <rect x="926" y="414" width="42" height="324" fill="url(#bar-green)"/>
      <ellipse cx="947" cy="738" rx="21" ry="5" fill="#2a7a36"/>
      <ellipse cx="947" cy="287" rx="21" ry="6" fill="#2567b0"/>
    </g>

    <text class="axis-gain" transform="translate(812 412) rotate(-90)">INCREASE YOUR</text>
    <text class="axis-cut" transform="translate(975 420) rotate(90)">DECREASE YOUR</text>

    <g class="gains">
      <text class="gain-label" x="861" y="82">Driver Safety</text>
      <text class="gain-label" x="882" y="131">Bottom Line Profit</text>
      <text class="gain-label" x="904" y="179">Capital spend</text>
      <text class="gain-label" x="925" y="227">Customer satisfaction</text>
      <text class="gain-label" x="955" y="274">Organisation Expectations</text>
    </g>

    <g class="cuts">
      <text class="cut-label" x="818" y="562">Carbon Footprints</text>
      <text class="cut-label" x="843" y="612">Business overheads</text>
      <text class="cut-label" x="870" y="661">Company risk</text>
      <text class="cut-label" x="906" y="708">Operations cost</text>
      <text class="cut-label" x="926" y="755">Speeding tickets</text>
    </g>
  </g>
</svg>
</body>
</html>
```